Graphic Design Project

I need to create a graphic design, which needs to be editable for me in Powerpoint... I have attached it a draft of it, but I need to be able to change the text of it. I want it to look more professional

Target Market(s)

Business Executives

Industry/Entity Type

Graphic Design

Requirements
Must have
• Make it look professional; the colors can change; I just need to be able to edit the text in powerpoint or either word

```html
<!DOCTYPE html>
<html lang="en">
<head>
<meta charset="utf-8">
<title>IT Vision &amp; Leadership Framework</title>
<link rel="stylesheet" href="https://fonts.googleapis.com/css2?family=Carlito:wght@400;700&display=swap">
<style>
  :root {
    --canvas: #ffffff;
    --ink: #161616;
    --banner-dark: #1d3657;
    --banner-light: #2e5079;
    --banner-text: #eef2f7;
    --shadow: rgba(60, 60, 60, 0.55);

    --vision-top: #bfe07e; --vision-front: #8fba4b; --vision-side: #6a9230;
    --ops-top: #3fcb73; --ops-front: #12b34d; --ops-side: #0b8c3a;
    --value-top: #a3bf72; --value-front: #7f9f45; --value-side: #5e7a30;
    --team-top: #e66e6e; --team-front: #c63b3b; --team-side: #962727;
    --rel-top: #fedcb9; --rel-front: #fcc898; --rel-side: #d8a274;
    --mkt-top: #f89d4c; --mkt-front: #f07a1c; --mkt-side: #c75e0b;
    --cust-top: #8cb8ef; --cust-front: #5d97e0; --cust-side: #3e72b5;
    --svc-top: #c9dcf4; --svc-front: #aac7eb; --svc-side: #88a1bf;
    --pol-top: #bfd6f5; --pol-front: #9fc1ee; --pol-side: #7e9dc4;
    --met-top: #e2ecfa; --met-front: #cfe0f5; --met-side: #a7b6cb;
  }
  * { box-sizing: border-box; margin: 0; padding: 0; }
  html, body { width: 1200px; height: 900px; overflow: hidden; background: var(--canvas); }
  .canvas { position: relative; width: 1200px; height: 900px; font-family: "Carlito", "Calibri", sans-serif; }
  .framework-art { position: absolute; inset: 0; }
  .block-label {
    position: absolute; display: flex; align-items: center; justify-content: center;
    text-align: center; font-weight: 700; font-size: 24px; line-height: 32px; color: var(--ink);
  }
  .block-label .label-text { display: block; white-space: nowrap; }
  .block-label .small { font-size: 21px; }
  .block-label .smaller { font-size: 20px; }
  .banner-title {
    position: absolute; left: 170px; top: 730px; width: 870px; height: 55px;
    display: flex; align-items: center; justify-content: center;
    font-size: 40px; font-weight: 700; letter-spacing: 1.5px; color: var(--banner-text);
  }
</style>
</head>
<body>
<div class="canvas">
  <svg class="framework-art" width="1200" height="900" viewBox="0 0 1200 900" aria-hidden="true">
    <defs>
      <filter id="soft-shadow" x="-50%" y="-100%" width="200%" height="300%"><feGaussianBlur stdDeviation="9"/></filter>
      <linearGradient id="banner-fill" x1="0" y1="0" x2="0" y2="1">
        <stop offset="0" stop-color="var(--banner-light)"/><stop offset="1" stop-color="var(--banner-dark)"/>
      </linearGradient>
      <linearGradient id="reflection-fade" x1="0" y1="0" x2="0" y2="1">
        <stop offset="0" stop-color="#fff" stop-opacity="0"/><stop offset="1" stop-color="#fff" stop-opacity="0.6"/>
      </linearGradient>
      <mask id="reflection-mask" maskUnits="userSpaceOnUse" x="0" y="700" width="1200" height="100">
        <rect x="0" y="700" width="1200" height="100" fill="url(#reflection-fade)"/>
      </mask>
    </defs>

    <g class="block-shadows" fill="var(--shadow)" filter="url(#soft-shadow)">
      <ellipse cx="540" cy="160" rx="55" ry="16"/>
      <ellipse cx="405" cy="330" rx="55" ry="16"/>
      <ellipse cx="644" cy="330" rx="55" ry="16"/>
      <ellipse cx="259" cy="507" rx="55" ry="16"/>
      <ellipse cx="512" cy="507" rx="55" ry="16"/>
      <ellipse cx="756" cy="507" rx="55" ry="16"/>
      <ellipse cx="147" cy="675" rx="55" ry="16"/>
      <ellipse cx="410" cy="675" rx="55" ry="16"/>
      <ellipse cx="653" cy="675" rx="55" ry="16"/>
      <ellipse cx="887" cy="665" rx="55" ry="16"/>
    </g>

    <g class="block block-vision">
      <polygon points="523,65 560,28 735,28 698,65" fill="var(--vision-top)"/>
      <polygon points="698,65 735,28 735,141 698,178" fill="var(--vision-side)"/>
      <rect x="523" y="65" width="175" height="113" fill="var(--vision-front)"/>
    </g>
    <g class="block block-ops">
      <polygon points="388,235 425,198 597,198 560,235" fill="var(--ops-top)"/>
      <polygon points="560,235 597,198 597,311 560,348" fill="var(--ops-side)"/>
      <rect x="388" y="235" width="172" height="113" fill="var(--ops-front)"/>
    </g>
    <g class="block block-value">
      <polygon points="627,235 664,198 836,198 799,235" fill="var(--value-top)"/>
      <polygon points="799,235 836,198 836,311 799,348" fill="var(--value-side)"/>
      <rect x="627" y="235" width="172" height="113" fill="var(--value-front)"/>
    </g>
    <g class="block block-team">
      <polygon points="242,411 279,374 452,374 415,411" fill="var(--team-top)"/>
      <polygon points="415,411 452,374 452,488 415,525" fill="var(--team-side)"/>
      <rect x="242" y="411" width="173" height="114" fill="var(--team-front)"/>
    </g>
    <g class="block block-relationship">
      <polygon points="495,411 532,374 705,374 668,411" fill="var(--rel-top)"/>
      <polygon points="668,411 705,374 705,488 668,525" fill="var(--rel-side)"/>
      <rect x="495" y="411" width="173" height="114" fill="var(--rel-front)"/>
    </g>
    <g class="block block-market">
      <polygon points="739,411 776,374 949,374 912,411" fill="var(--mkt-top)"/>
      <polygon points="912,411 949,374 949,488 912,525" fill="var(--mkt-side)"/>
      <rect x="739" y="411" width="173" height="114" fill="var(--mkt-front)"/>
    </g>
    <g class="block block-customer">
      <polygon points="130,580 167,543 340,543 303,580" fill="var(--cust-top)"/>
      <polygon points="303,580 340,543 340,656 303,693" fill="var(--cust-side)"/>
      <rect x="130" y="580" width="173" height="113" fill="var(--cust-front)"/>
    </g>
    <g class="block block-service">
      <polygon points="393,580 430,543 603,543 566,580" fill="var(--svc-top)"/>
      <polygon points="566,580 603,543 603,656 566,693" fill="var(--svc-side)"/>
      <rect x="393" y="580" width="173" height="113" fill="var(--svc-front)"/>
    </g>
    <g class="block block-policy">
      <polygon points="636,580 673,543 846,543 809,580" fill="var(--pol-top)"/>
      <polygon points="809,580 846,543 846,656 809,693" fill="var(--pol-side)"/>
      <rect x="636" y="580" width="173" height="113" fill="var(--pol-front)"/>
    </g>
    <g class="block block-metrics">
      <polygon points="870,570 907,533 1080,533 1043,570" fill="var(--met-top)"/>
      <polygon points="1043,570 1080,533 1080,646 1043,683" fill="var(--met-side)"/>
      <rect x="870" y="570" width="173" height="113" fill="var(--met-front)"/>
    </g>

    <polygon class="banner" points="170,730 1040,730 1000,785 210,785" fill="url(#banner-fill)"/>

    <g class="banner-reflection" transform="translate(0,1600) scale(1,-1)">
      <g mask="url(#reflection-mask)">
        <polygon points="170,730 1040,730 1000,785 210,785" fill="#b9c3cf"/>
        <text x="605" y="772" text-anchor="middle" font-family="Carlito, Calibri, sans-serif" font-weight="700" font-size="40" letter-spacing="1.5" fill="#ffffff">MANAGING CHANGE</text>
      </g>
    </g>
  </svg>

  <div class="block-label" style="left:523px;top:65px;width:175px;height:113px"><span class="label-text">IT VISION &amp;<br>LEADERSHIP</span></div>
  <div class="block-label" style="left:388px;top:235px;width:172px;height:113px"><span class="label-text">Maintain IT<br>Operational<br>Excellence</span></div>
  <div class="block-label" style="left:627px;top:235px;width:172px;height:113px"><span class="label-text">Create<br>Business<br>Value</span></div>
  <div class="block-label" style="left:242px;top:411px;width:173px;height:114px"><span class="label-text">Transform IT<br>Team</span></div>
  <div class="block-label" style="left:495px;top:411px;width:173px;height:114px"><span class="label-text">Master<br>Relationship<br>Management</span></div>
  <div class="block-label" style="left:739px;top:411px;width:173px;height:114px"><span class="label-text">Market &amp;<br><span class="small">Communicate</span><br>Value</span></div>
  <div class="block-label" style="left:130px;top:580px;width:173px;height:113px"><span class="label-text">Customer<br>Engagement<br>Model</span></div>
  <div class="block-label" style="left:393px;top:580px;width:173px;height:113px"><span class="label-text">Service-<br>Minded<br>IT Culture</span></div>
  <div class="block-label" style="left:636px;top:580px;width:173px;height:113px"><span class="label-text">Policy,<br>Process &amp;<br><span class="smaller">Methodologies</span></span></div>
  <div class="block-label" style="left:870px;top:570px;width:173px;height:113px"><span class="label-text">Meaningful<br>Metrics</span></div>

  <div class="banner-title">MANAGING CHANGE</div>
</div>
</body>
</html>
```